New template needed for Joomla 3.2 website

We are a mortgage origination company based in Johannesburg, South Africa and require a sleek, modern & professional look for our website.
The website is complete and your template should accommodate all pages on the site (there are not many) and be ready for Joomla implementation.
Our website can be viewed at www.kestrelbondhouse.co.za
Target Market(s)
We are targeting consumers who require mortgage finance to buy real estate. There is no particular demographic, except that we cater to South African home buyers exclusively!
Requirements
Must have
- It must look professional and modern.
Take a look at competitor websites:
www.ziru.co.za
www.velmabonds.com
http://www.tarnvalegroup.co.za/lendcrest/
http://www.quillfund.co.za/
We want to beat the competition !!
Nice to have
- Website should blend with company logo and play on the symbol in the logo.
I want more of a people / photo element to the template. It needs to make us seem "tangible"

```html
<!DOCTYPE html>
<html lang="en">
<head>
<meta charset="utf-8">
<title>Kestrel Bond House – Property Finance Made Easy</title>
<link href="https://fonts.googleapis.com/css2?family=Lato:wght@300;400;700&display=swap" rel="stylesheet">
<style>
:root{
  --blue:#1a8fd0;
  --nav:#16a0e0;
  --navy:#2a55a8;
  --red:#d0141b;
  --ink:#222;
  --text:#555;
  --grey-band:#efefef;
  --white:#fff;
  --teal:#2bab8e;
  --coral:#e04a3b;
  --gold:#f5c500;
  --slate:#3d4752;
  --aqua:#2aa3a8;
  --green-btn:#3ec99b;
}
*{margin:0;padding:0;box-sizing:border-box}
html,body{width:815px;height:1200px;overflow:hidden;background:var(--white)}
body{font-family:'Lato',sans-serif;color:var(--text);position:relative}
.abs{position:absolute}

/* header */
.site-header{position:absolute;left:0;top:0;width:815px;height:58px}
.brand{left:110px;top:12px;display:flex;align-items:center;gap:6px}
.brand-dot{width:26px;height:26px;border-radius:50%;background:var(--blue)}
.brand-name{font-size:15px;font-weight:700;color:var(--blue);line-height:1}
.brand-tag{font-size:7px;font-weight:700;color:var(--navy);letter-spacing:.2px;margin-top:2px}
.contact{right:109px;top:9px;text-align:right}
.contact-phone{font-size:11px;color:var(--blue)}
.contact-lead{font-size:9.5px;font-weight:700;color:var(--ink);margin-top:3px}
.lenders{font-size:7.5px;color:#666;margin-top:3px;letter-spacing:.2px}

.main-nav{top:58px;left:0;width:815px;height:21px;background:var(--nav);display:flex;align-items:center;padding-left:115px;gap:10px}
.main-nav a{color:var(--white);text-decoration:none;font-size:8px}

/* hero */
.hero{top:79px;left:0;width:815px;height:245px;
  background:
    radial-gradient(ellipse 300px 170px at 420px 170px, rgba(214,160,128,.85) 0%, rgba(226,186,160,.55) 45%, rgba(230,225,222,0) 100%),
    radial-gradient(ellipse 120px 150px at 510px 90px, rgba(232,196,160,.75) 0%, rgba(232,220,210,0) 100%),
    linear-gradient(180deg,#dcdcdc 0%,#e9e7e5 60%,#f1f0ef 100%)}
.hero-title{left:228px;top:16px;color:var(--red);font-size:23px;line-height:1;text-align:right;font-weight:400}
.hero-title span{display:block;font-size:16px;margin-top:1px;font-weight:300}

/* features */
.section-title{top:360px;left:0;width:815px;text-align:center;font-size:19px;color:var(--ink);font-weight:400}
.feature{top:404px;width:190px;text-align:center}
.icon{width:46px;height:46px;border-radius:50%;margin:0 auto;display:flex;align-items:center;justify-content:center}
.feature h3{font-size:12px;color:var(--blue);font-weight:400;margin-top:12px}
.feature p{font-size:9px;line-height:13px;margin-top:9px;font-weight:300;color:#444}

/* intro band */
.intro-band{top:617px;left:0;width:815px;height:168px;background:var(--grey-band)}
.intro-col{top:646px;width:192px}
.intro-col h2{font-size:12px;font-weight:400;color:var(--blue)}
.intro-col p{font-size:7px;line-height:12px;margin-top:5px;color:#444}
.callback{top:617px;left:517px;width:189px;height:168px;background:var(--navy);border:1px solid #1f4590;padding:12px 10px 0}
.callback h2{font-size:12px;font-weight:400;color:var(--white);line-height:14px}
.field-row{display:flex;gap:5px;margin-top:4px}
.callback .first{margin-top:7px}
.field{height:17px;border:1px solid #6f8fcf;background:#3a63b2;color:var(--white);font-size:7px;line-height:15px;padding:0 4px;flex:1}
.field.select{position:relative}
.field.select:after{content:"";position:absolute;right:6px;top:6px;border:3px solid transparent;border-top-color:#9bb3e3}
.field.comment{height:38px}
.btn-send{margin-top:6px;display:inline-block;background:var(--green-btn);color:var(--white);font-size:9px;line-height:18px;height:18px;padding:0 7px}

/* programs */
.program-art{width:88px;height:88px;border-radius:50%}
.program{top:823px;width:190px}
.program h2{font-size:12px;font-weight:400;color:var(--blue)}
.program p{font-size:9px;line-height:13px;margin-top:9px;font-weight:300;color:#444}

/* actions */
.actions-band{top:953px;left:0;width:815px;height:214px;background:var(--grey-band)}
.action{top:984px;width:138px}
.action .icon{margin:0}
.action h3{font-size:12px;font-weight:400;color:var(--blue);margin-top:15px}
.action p{font-size:9px;line-height:13px;margin-top:4px;font-weight:300;color:#444;height:53px}
.action-btn{display:flex;justify-content:space-between;align-items:center;background:var(--white);border:1px solid #ddd;height:18px;padding:0 6px;font-size:8.5px;color:var(--blue);width:137px}

/* footer */
.site-footer{top:1167px;left:0;width:815px;height:33px;background:var(--navy);display:flex;justify-content:center;align-items:center;gap:5px;font-size:7px;color:#dfe6f5}
.site-footer strong{color:var(--white);margin-left:3px}
</style>
</head>
<body>

<header class="site-header">
  <div class="abs brand">
    <div class="brand-dot"></div>
    <div>
      <div class="brand-name">KESTREL BOND HOUSE</div>
      <div class="brand-tag">PROPERTY FINANCE MADE EASY</div>
    </div>
  </div>
  <div class="abs contact">
    <div class="contact-phone">Call: (010) 482 7315</div>
    <div class="contact-lead">We raise your homeloan with:</div>
    <div class="lenders">QBN • HALVERBANK • ORVA • MERIDIAN • VELMA BONDS • TRB • CALDERTEC</div>
  </div>
</header>

<nav class="abs main-nav">
  <a href="#">Home</a><a href="#">About Kestrel</a><a href="#">Important Information</a><a href="#">Homeloan Calculators</a><a href="#">Apply On-Line</a><a href="#">Contact Kestrel</a>
</nav>

<section class="abs hero" role="img" aria-label="Photo of a smiling young family of four, two parents and two children, lying together on a white bed">
  <h1 class="abs hero-title">PROPERTY FINANCE<span>MADE EASY</span></h1>
</section>

<h2 class="abs section-title">Fast Homeloans. Great Service!</h2>

<div class="abs feature" style="left:109px">
  <div class="icon" style="background:var(--teal)">
    <svg width="24" height="24" viewBox="0 0 24 24"><rect x="3" y="3" width="18" height="18" rx="2" fill="#eee"/><rect x="6" y="6" width="9" height="12" fill="#ccc"/><circle cx="18" cy="12" r="1.5" fill="#888"/></svg>
  </div>
  <h3>100% Free of Charge</h3>
  <p>No hidden costs or service charges. Our fee is not hidden within the finance charges of your homeloan. We guarantee a 100% free of charge, first class service to you. Our fees are paid by the banks, regardless of your homeloan.</p>
</div>
<div class="abs feature" style="left:315px">
  <div class="icon" style="background:var(--coral)">
    <svg width="24" height="24" viewBox="0 0 24 24"><circle cx="12" cy="10" r="7" fill="#f3b43c"/><circle cx="12" cy="10" r="4" fill="#e89b1c"/><path d="M8 16l-2 6 4-2 2 2 0-6zM16 16l2 6-4-2-2 2 0-6z" fill="#f3b43c"/></svg>
  </div>
  <h3>Exceptional Service</h3>
  <p>We guarantee a first class service to you. Our home loan specialists are up to date with the latest finance criteria from all the major financial institutions. We fight for your bond and strive to secure the very best deal possible on your behalf!</p>
</div>
<div class="abs feature" style="left:519px;width:186px">
  <div class="icon" style="background:var(--gold)">
    <svg width="24" height="24" viewBox="0 0 24 24"><rect x="7" y="3" width="10" height="19" rx="2" fill="#4a5563"/><rect x="9" y="5" width="6" height="5" fill="#8fd0e8"/></svg>
  </div>
  <h3>Credit Help</h3>
  <p>Problems with your credit record? We will do our best to help you into the clear with sound advice. We will refer you to attorneys and other business partners who specialise in the removal of adverse credit information. Let us work together and solve the problems to obtain your homeloan finance.</p>
</div>

<section class="abs intro-band"></section>
<div class="abs intro-col" style="left:110px">
  <h2>Welcome to Kestrel Bond House</h2>
  <p>Purchasing property is an exciting adventure for first time homebuyers and experienced property connoisseurs akin. Regardless of experience in the property market, we share one common expectation in that we want exceptional service from the professionals who assist us. An uncomplicated property transaction means that you can focus time and money on your new property, preparing it for your occupation or a tenanted rental.</p>
</div>
<div class="abs intro-col" style="left:313px">
  <h2>Why use Kestrel Bond House</h2>
  <p>Purchasing property is an exciting adventure for first time homebuyers and experienced property connoisseurs akin. Regardless of experience in the property market, we share one common expectation in that we want exceptional service from the professionals who assist us. An uncomplicated property transaction means that you can focus time and money on your new property, preparing it for your occupation or a tenanted rental.</p>
</div>
<form class="abs callback">
  <h2>Call Me Back</h2>
  <div class="field-row first"><div class="field">First Name</div><div class="field">Last Name</div></div>
  <div class="field-row"><div class="field">E-mail</div><div class="field">Phone</div></div>
  <div class="field-row"><div class="field select">Nature of Enquiry</div></div>
  <div class="field-row"><div class="field comment">Comment</div></div>
  <div class="btn-send">Contact Me</div>
</form>

<div class="abs program-art" style="left:108px;top:825px;background:radial-gradient(circle,#e9f4fb 0%,#cfe6f4 100%);border:2px solid #b9daf0" role="img" aria-label="Illustration of a network of connected people"></div>
<div class="abs program" style="left:211px">
  <h2>Kestrel Lead Referral Program</h2>
  <p>We invite members of the public, estate agents, attorneys, property developers and all other property professionals to refer leads to us. Why not join our referal program and earn money for every successful lead. It pays!</p>
</div>
<div class="abs program-art" style="left:415px;top:825px;background:radial-gradient(circle,#8fb9f0 0%,#5f97e6 100%)" role="img" aria-label="Illustration of a hand holding a bank card"></div>
<div class="abs program" style="left:516px">
  <h2>Kestrel Paycrest Card</h2>
  <p>All members of our lead referal program will receive a Kestrel Paycrest card. We will load money earned from referals to your card and for you to spend in any way you please! These Paycrest cards are accepted in all retail stores</p>
</div>

<section class="abs actions-band"></section>
<div class="abs action" style="left:108px">
  <div class="icon" style="background:var(--slate);width:48px;height:48px">
    <svg width="28" height="28" viewBox="0 0 28 28" fill="none" stroke-width="2.5"><circle cx="11" cy="11" r="6" stroke="#e0574a"/><circle cx="17" cy="11" r="6" stroke="#3bb3c3"/><circle cx="14" cy="17" r="6" stroke="#e9b949"/></svg>
  </div>
  <h3>Referral Program</h3>
  <p>Click on the button below to join our lead referal program and start earning money.</p>
  <div class="action-btn">Join Today<svg width="6" height="8" viewBox="0 0 6 8"><path d="M1 1l3 3-3 3" stroke="var(--blue)" stroke-width="1.6" fill="none"/></svg></div>
</div>
<div class="abs action" style="left:262px">
  <div class="icon" style="background:var(--gold);width:48px;height:48px">
    <svg width="28" height="28" viewBox="0 0 28 28"><path d="M6 22l3-8 12-10 4 4-12 10z" fill="#e0574a"/><path d="M6 22l3-8 4 4z" fill="#f6d9a8"/></svg>
  </div>
  <h3>Get Pre Qualified</h3>
  <p>Our experienced consultants would be happy to prequalify you for a homeloan.</p>
  <div class="action-btn">Apply Now<svg width="6" height="8" viewBox="0 0 6 8"><path d="M1 1l3 3-3 3" stroke="var(--blue)" stroke-width="1.6" fill="none"/></svg></div>
</div>
<div class="abs action" style="left:415px">
  <div class="icon" style="background:var(--aqua);width:48px;height:48px">
    <svg width="28" height="28" viewBox="0 0 28 28"><text x="14" y="21" text-anchor="middle" font-family="Lato,sans-serif" font-size="20" font-weight="700" fill="#fff">?</text></svg>
  </div>
  <h3>Ask a Question</h3>
  <p>Ask an experienced consultant to answer all your questions about homeloan finance.</p>
  <div class="action-btn">Ask Now<svg width="6" height="8" viewBox="0 0 6 8"><path d="M1 1l3 3-3 3" stroke="var(--blue)" stroke-width="1.6" fill="none"/></svg></div>
</div>
<div class="abs action" style="left:568px">
  <div class="icon" style="background:var(--slate);width:48px;height:48px">
    <svg width="28" height="28" viewBox="0 0 28 28" stroke-width="2.5" stroke-linecap="round"><path d="M9 4v9M4.5 8.5h9" stroke="#e9b949"/><path d="M16 8.5h8" stroke="#e0574a"/><path d="M5 17l7 7M12 17l-7 7" stroke="#3bb3c3"/><path d="M16 20.5h8" stroke="#eee"/><circle cx="20" cy="17" r="1" fill="#eee"/><circle cx="20" cy="24" r="1" fill="#eee"/></svg>
  </div>
  <h3>Calculators</h3>
  <p>Find out what you can afford with our convenient finance calculators.</p>
  <div class="action-btn">Calculate<svg width="6" height="8" viewBox="0 0 6 8"><path d="M1 1l3 3-3 3" stroke="var(--blue)" stroke-width="1.6" fill="none"/></svg></div>
</div>

<footer class="abs site-footer">
  <span>Privacy Policy</span><span>About Kestrel</span><span>Contact Kestrel</span><strong>Copyright © 2014 Kestrel Bond House (Pty) Ltd</strong>
</footer>

</body>
</html>
```